Face lift needed for client website www.vorthanmed.com

vorthanmed is Dallas based medical device company. 1. Would like to see a home page design that stays to the company colors (blue, gray, white, black). Home page is boring. Need lively pate with active people background who could benefit from the products. Compare with www.quelbrintex.com and www.parnivo.com. 2. Would like new looks for each of "Our Company" (i.e. our philosophy / our management team).

Industry/Entity Type

Medical

```html
<!DOCTYPE html>
<html lang="en">
<head>
<meta charset="utf-8">
<title>vorthanmed – Home</title>
<link href="https://fonts.googleapis.com/css2?family=Open+Sans:wght@400;600;700&family=Roboto+Condensed:wght@400;700&display=swap" rel="stylesheet">
<style>
  :root {
    --brand-blue: #2b6cb0;
    --brand-blue-dark: #1f4f86;
    --news-blue: #2f69a3;
    --ink: #1c1c1c;
    --text-gray: #555b61;
    --nav-gray: #6d7378;
    --line-gray: #d9dcdf;
    --band-gray: #c9cccf;
    --quote-gray: #9a9ea2;
    --white: #ffffff;
  }
  * { box-sizing: border-box; margin: 0; padding: 0; }
  html, body { width: 1200px; height: 686px; overflow: hidden; background: var(--white); }
  body { font-family: "Open Sans", Arial, sans-serif; color: var(--text-gray); position: relative; }

  .site-header { position: absolute; left: 0; top: 0; width: 1200px; height: 64px; display: flex; align-items: center; justify-content: space-between; padding: 0 40px; }
  .brand-name { font-family: "Roboto Condensed", Arial, sans-serif; font-weight: 700; font-size: 30px; color: var(--brand-blue); line-height: 1; }
  .search { display: flex; align-items: center; width: 200px; height: 22px; border: 1px solid var(--line-gray); border-radius: 11px; overflow: hidden; }
  .search-field { flex: 1; }
  .search-button { width: 34px; height: 100%; background: var(--nav-gray); display: flex; align-items: center; justify-content: center; }

  .main-nav { position: absolute; left: 40px; top: 64px; width: 1120px; height: 28px; display: flex; justify-content: space-between; align-items: center; border-top: 1px solid var(--line-gray); }
  .main-nav a { font-size: 10px; font-weight: 600; color: var(--nav-gray); text-decoration: none; letter-spacing: .5px; }
  .main-nav a.current { color: var(--brand-blue); }

  .hero { position: absolute; left: 0; top: 92px; width: 1200px; height: 208px; background: linear-gradient(180deg, #a9b98c 0%, #7fa14f 45%, #5e8b34 100%); }
  .hero-photo { position: absolute; inset: 0; background: linear-gradient(90deg, rgba(255,255,255,0) 60%, rgba(232,196,170,.55) 85%, rgba(225,185,160,.8) 100%); }
  .hero-title { position: absolute; left: 360px; top: 30px; font-family: "Roboto Condensed", Arial, sans-serif; font-size: 30px; color: var(--brand-blue-dark); }
  .hero-dots { position: absolute; left: 50px; bottom: 14px; display: flex; gap: 8px; }
  .hero-dots span { width: 9px; height: 9px; border-radius: 50%; background: rgba(255,255,255,.6); }
  .hero-dots span.active { background: var(--brand-blue); }

  .intro { position: absolute; left: 40px; top: 308px; width: 810px; }
  .section-title { font-family: "Roboto Condensed", Arial, sans-serif; font-size: 20px; color: var(--brand-blue); margin-bottom: 4px; }
  .intro p, .philosophy p { font-size: 10.5px; line-height: 1.45; }
  .intro strong { color: var(--brand-blue); }
  .lifestyle-photos { display: flex; gap: 28px; margin: 8px 0 0 40px; }
  .lifestyle-photo { width: 72px; height: 72px; border-radius: 50%; border: 3px solid var(--white); box-shadow: 0 0 0 1px var(--line-gray); }
  .photo-office { background: radial-gradient(circle at 50% 40%, #d9c4b0, #9aa3ab); }
  .photo-couple { background: radial-gradient(circle at 50% 40%, #e2b795, #6f9b48); }
  .photo-play { background: radial-gradient(circle at 50% 40%, #5f86b8, #6a9a3c); }
  .philosophy { position: absolute; left: 40px; top: 472px; width: 810px; }

  .latest-news { position: absolute; left: 880px; top: 300px; width: 280px; height: 262px; background: var(--news-blue); color: var(--white); padding: 10px 16px; }
  .latest-news h2 { font-family: "Roboto Condensed", Arial, sans-serif; font-size: 15px; letter-spacing: 1px; margin-bottom: 6px; }
  .news-item { border-top: 1px solid rgba(255,255,255,.35); padding: 5px 0; font-size: 8.5px; line-height: 1.35; }
  .news-item h3 { font-size: 9px; font-weight: 700; }
  .read-more { display: block; margin: 3px 0 0 auto; width: 58px; text-align: center; background: var(--white); color: var(--news-blue); border-radius: 8px; font-size: 8px; font-weight: 700; }
  .more-news { text-align: right; font-size: 9px; font-weight: 700; margin-top: 2px; }

  .management { position: absolute; left: 0; top: 562px; width: 1200px; height: 94px; background: linear-gradient(180deg, #e4e6e8, var(--band-gray)); }
  .management .section-title { position: absolute; left: 40px; top: 10px; }
  .team-photo { position: absolute; left: 300px; top: 0; width: 520px; height: 94px; background: linear-gradient(90deg, rgba(60,65,72,0) 0%, #4a5058 20%, #2c3138 50%, #4a5058 80%, rgba(60,65,72,0) 100%); }
  .leader { position: absolute; left: 850px; top: 22px; font-size: 10px; color: var(--ink); }
  .leader strong { display: block; color: var(--brand-blue-dark); }

  .quote-bar { position: absolute; left: 0; top: 656px; width: 1200px; height: 30px; background: var(--quote-gray); display: flex; align-items: center; justify-content: center; gap: 10px; font-size: 11px; color: var(--ink); }
  .quote-bar cite { font-style: italic; }
</style>
</head>
<body>
  <header class="site-header">
    <div class="brand-name">vorthanmed</div>
    <div class="search">
      <span class="search-field"></span>
      <span class="search-button">
        <svg width="12" height="12" viewBox="0 0 12 12"><circle cx="5" cy="5" r="3.5" fill="none" stroke="#fff" stroke-width="1.5"/><line x1="7.6" y1="7.6" x2="11" y2="11" stroke="#fff" stroke-width="1.5"/></svg>
      </span>
    </div>
  </header>

  <nav class="main-nav">
    <a class="current" href="#">HOME</a>
    <a href="#">OUR COMPANY</a>
    <a href="#">PRODUCTS</a>
    <a href="#">NEWS ROOM</a>
    <a href="#">CONTACT US</a>
  </nav>

  <section class="hero">
    <div class="hero-photo" role="img" aria-label="Woman in a pink top doing a push-up on a mat in a grassy park, with a close-up of a lower back at the right"></div>
    <h1 class="hero-title">Healing people with spinal disorders.</h1>
    <div class="hero-dots"><span class="active"></span><span></span><span></span></div>
  </section>

  <section class="intro">
    <h2 class="section-title">Active For Life</h2>
    <p><strong>vorthanmed</strong> is a forward thinking medical device company that strives to develop products and services that treat spinal disorders. The vorthanmed Portfolio showcases a wide range of complementary products that include a minimally invasive spine system, posterior cervical system, thoracolumbar systems, anterior cervical plate system, interbody device options, and biologic solutions.</p>
    <div class="lifestyle-photos">
      <div class="lifestyle-photo photo-office" role="img" aria-label="Man working at a laptop"></div>
      <div class="lifestyle-photo photo-couple" role="img" aria-label="Smiling couple outdoors"></div>
      <div class="lifestyle-photo photo-play" role="img" aria-label="Father and child playing football"></div>
    </div>
  </section>

  <section class="philosophy">
    <h2 class="section-title">Our Philosophy</h2>
    <p>At vorthanmed, we believe patients deserve care that restores motion and confidence. Our teams work closely with surgeons to design solutions that improve outcomes and help people return to the lives they love.</p>
  </section>

  <aside class="latest-news">
    <h2>LATEST NEWS</h2>
    <article class="news-item">
      <h3>Meet the Spine &amp; Pain Team at the Fall Surgical Congress</h3>
      <p>Visit our booth to see new cervical and lumbar systems in action.</p>
      <span class="read-more">Read more</span>
    </article>
    <article class="news-item">
      <h3>vorthanmed Signs New Distribution Agreement</h3>
      <p>The partnership brings our interbody devices to new clinics across Texas.</p>
      <span class="read-more">Read more</span>
    </article>
    <article class="news-item">
      <h3>New Study Confirms Faster Patient Recovery</h3>
      <p>Results show shorter hospital stays with our minimally invasive system.</p>
      <span class="read-more">Read more</span>
    </article>
    <div class="more-news">MORE NEWS &#8250;</div>
  </aside>

  <section class="management">
    <h2 class="section-title">Management Team</h2>
    <div class="team-photo" role="img" aria-label="Group portrait of the management team in business attire"></div>
    <div class="leader"><strong>Daniel Orsin</strong>President &amp; CEO</div>
  </section>

  <footer class="quote-bar">
    <q>A life is not important except in the impact it has on other lives.</q>
    <cite>– Marlon Tesh</cite>
  </footer>
</body>
</html>
```